PPC Landing Page For Technology Consultant

Looking for a high converting landing page for PPC and other Web Marketing traffic. Main objective is to complete a contact form on the main page (preferably at the top built into header image but open to ideas).

WORDPRESS ONLY. All Elements from Website (www.linkvantor.example) are available in adobe format)

Target Market(s)

IT Professionals in mid market and enterprise industries

Industry/Entity Type

It Service

Font styles to use
Sans Serif

Requirements
Must have
• Wordpress theme, customizable and re-usable. Will need help implementing the new site in our wordpress subdomain.
• Contact Form prominent and highlighted, as well as other call to actions (call, get a quote etc.)
Nice to have
• Scrolling logo list of our partners, or some other way to highlight to the our deep portfolio of providers (http://www.linkvantor.example/our-suppliers/), Products, Services etc.
• Some Testimonial section would be nice as well.

```html
<!DOCTYPE html>
<html lang="en">
<head>
<meta charset="utf-8">
<title>Linkvantor – Technology Solutions</title>
<link href="https://fonts.googleapis.com/css2?family=Oswald:wght@400;500;700&family=Open+Sans:wght@400;600;700&display=swap" rel="stylesheet">
<style>
:root{
  --blue:#0b4ea2;
  --blue-dark:#094590;
  --orange:#f7841e;
  --ink:#222;
  --muted:#444;
  --soft:#f4f2f2;
  --footer:#1c1819;
  --line:#c9c9c9;
}
*{box-sizing:border-box;margin:0;padding:0}
html,body{width:1200px;height:4038px;overflow:hidden}
body{font-family:"Open Sans",Arial,sans-serif;color:var(--ink);background:#fff;position:relative}
.abs{position:absolute}
.heading{font-family:"Oswald",Arial Narrow,sans-serif;font-weight:400;text-transform:uppercase;color:var(--ink)}
.section-title{position:absolute;left:0;width:1200px;text-align:center;font-size:32px;line-height:1.35;letter-spacing:-.3px}
.title-rule{position:absolute;left:579px;width:42px;height:3px;background:var(--blue)}
.btn{position:absolute;background:var(--orange);color:#fff;font-weight:700;text-transform:uppercase;display:flex;align-items:center;justify-content:center;letter-spacing:.3px}

/* header */
.site-header{position:absolute;top:0;left:0;width:1200px;height:99px;background:#fff}
.brand{position:absolute;left:130px;top:20px;font-family:"Oswald",sans-serif;font-weight:700;font-size:44px;line-height:1;color:var(--orange);letter-spacing:-.5px}
.call{position:absolute;left:683px;top:20px;display:flex;gap:10px;align-items:center}
.call small{display:block;font-size:11px;color:var(--ink);font-weight:600}
.call strong{display:block;font-size:17px;color:var(--blue);font-weight:600;letter-spacing:.3px}
.btn-quote{left:885px;top:22px;width:94px;height:28px;font-size:12px}
.btn-login{position:absolute;left:999px;top:22px;width:71px;height:28px;border:2px solid var(--blue);color:var(--blue);font-size:12px;font-weight:600;display:flex;align-items:center;justify-content:center}
.main-nav{position:absolute;left:459px;top:67px;width:612px;display:flex;justify-content:space-between;font-size:13px;font-weight:600}
.main-nav .active{color:var(--orange)}

/* hero */
.hero{position:absolute;top:99px;left:0;width:1200px;height:543px;background:linear-gradient(120deg,#c9ccd1 0%,#e9e9ea 35%,#8a8f98 62%,#3b4350 100%)}
.hero-band{position:absolute;top:172px;left:0;width:640px;height:175px;background:rgba(11,78,162,.86)}
.hero h1{position:absolute;left:130px;top:192px;font-family:"Oswald",sans-serif;font-weight:500;font-size:44px;color:#fff;line-height:1}
.hero p{position:absolute;left:130px;top:246px;width:460px;font-size:15px;line-height:1.3;color:#fff}
.btn-hero{left:130px;top:297px;width:118px;height:33px;font-size:14px}
.dots{position:absolute;top:492px;left:549px;display:flex;gap:12px}
.dots span{width:10px;height:10px;border-radius:50%;background:#fff;opacity:.85}
.dots .on{background:var(--orange);border:2px solid #fff;opacity:1}

/* solutions */
.solutions{position:absolute;top:642px;left:0;width:1200px;height:502px;background:var(--soft)}
.sol-card{position:absolute;top:152px;width:220px;height:295px;background:#fff;text-align:center;box-shadow:0 2px 6px rgba(0,0,0,.06)}
.sol-card svg{margin-top:34px}
.sol-card h3{margin-top:26px;font-size:14px;font-weight:600;text-transform:uppercase}
.sol-card p{margin:20px auto 0;width:170px;font-size:12.5px;line-height:1.4;color:var(--muted)}
.sol-card .btn{left:66px;top:237px;width:89px;height:24px;font-size:12px}

/* value band */
.value{position:absolute;top:1144px;left:0;width:1200px;height:514px;background:var(--blue)}
.value h2{position:absolute;left:130px;top:88px;font-family:"Oswald",sans-serif;font-weight:400;font-size:46px;line-height:1.22;color:#fff;text-transform:uppercase}
.value .lead{position:absolute;left:130px;top:218px;width:340px;font-size:22px;line-height:1.38;color:#fff;text-transform:uppercase}
.btn-value{left:132px;top:346px;width:166px;height:47px;font-size:17px}
.tile{position:absolute;width:160px;height:130px;background:#fff;text-align:center;font-size:12px;line-height:1.35;color:var(--ink)}
.tile svg{display:block;margin:22px auto 10px}

/* consulting */
.consult h2{top:1716px}
.adv-card{position:absolute;top:1875px;width:270px;height:298px;border:1px solid var(--line);text-align:center;background:#fff}
.adv-card svg{margin-top:34px}
.adv-card h3{margin-top:24px;font-size:14px;font-weight:600;text-transform:uppercase}
.adv-card p{margin:18px auto 0;width:225px;font-size:12.5px;line-height:1.42;color:var(--muted)}

/* testimonials */
.testimonials{position:absolute;top:2243px;left:0;width:1200px;height:566px;background:var(--soft)}
.quote-card{position:absolute;top:170px;width:300px;height:330px;background:#fff;box-shadow:0 2px 6px rgba(0,0,0,.07);padding:24px 36px 0 36px}
.qmark{font-family:Georgia,serif;font-size:30px;color:#bbb;line-height:1;height:20px}
.quote-card p{margin-top:6px;font-size:12.5px;line-height:1.45;color:var(--muted)}
.qend{text-align:right;font-family:Georgia,serif;font-size:30px;color:#bbb;line-height:1;height:20px}
.who{position:absolute;left:36px;top:268px;font-size:12px;line-height:1.55;text-transform:uppercase}
.who b{font-weight:700}
.arrow{position:absolute;font-size:34px;color:#b5b5b5;font-weight:300}

/* partners */
.partners h2{top:2869px}
.logos{position:absolute;top:2985px;left:130px;width:940px;display:flex;justify-content:space-between;align-items:center}
.logo-name{display:flex;align-items:center;gap:7px;font-size:20px;font-weight:700;color:#5a6470}
.logo-name i{width:14px;height:14px;background:#9aa5b1;border-radius:50%;display:inline-block}

/* quote form */
.quote-form{position:absolute;top:3105px;left:0;width:1200px;height:530px;background:var(--blue)}
.quote-form .section-title{color:#fff;top:47px}
.quote-form .title-rule{background:#fff;top:104px}
.field{position:absolute;border:2px solid #fff;color:#fff;font-size:14px;font-weight:600;text-transform:uppercase;padding:14px 20px}
.btn-send{left:518px;top:436px;width:165px;height:46px;font-size:17px}

/* footer */
.site-footer{position:absolute;top:3635px;left:0;width:1200px;height:403px;background:var(--footer);color:#fff}
.footer-brand{position:absolute;left:130px;top:143px;font-family:"Oswald",sans-serif;font-weight:700;font-size:44px;line-height:1;color:var(--orange)}
.footer-col{position:absolute;top:60px}
.footer-col h4{font-size:14px;font-weight:700;letter-spacing:.5px;margin-bottom:26px}
.footer-col ul{list-style:none;font-size:13px;line-height:24px}
.contact-row{display:flex;gap:12px;align-items:center;font-size:13px;line-height:1.45;margin-bottom:18px}
.circ{width:28px;height:28px;border-radius:50%;background:#fff;display:flex;align-items:center;justify-content:center;flex:none}
.footer-rule{position:absolute;left:130px;top:322px;width:940px;height:1px;background:#3a3536}
.copyright{position:absolute;top:355px;left:0;width:1200px;text-align:center;font-size:11px;color:#ddd}
</style>
</head>
<body>

<header class="site-header">
  <div class="brand">Linkvantor</div>
  <div class="call">
    <svg width="26" height="26" viewBox="0 0 24 24"><path fill="#0b4ea2" d="M6.6 10.8a15.1 15.1 0 0 0 6.6 6.6l2.2-2.2c.3-.3.7-.4 1-.2 1.1.4 2.3.6 3.6.6.6 0 1 .4 1 1V20c0 .6-.4 1-1 1A17 17 0 0 1 3 4c0-.6.4-1 1-1h3.5c.6 0 1 .4 1 1 0 1.3.2 2.5.6 3.6.1.3 0 .7-.2 1z"/></svg>
    <div><small>CALL US</small><strong>1-888-555-0142</strong></div>
  </div>
  <div class="btn btn-quote">Get Quote</div>
  <div class="btn-login">LOGIN</div>
  <nav class="main-nav">
    <span class="active">TECHNOLOGY SOLUTIONS</span><span>SUPPLIERS</span><span>TESTIMONIALS</span><span>PARTNERSHIP</span><span>CONTACT US</span>
  </nav>
</header>

<section class="hero" role="img" aria-label="Photo of a person working on a laptop showing bar and pie charts beside a coffee mug and printed reports">
  <div class="hero-band"></div>
  <h1>WEB MARKETING TRAFFIC</h1>
  <p>Leverage better-than-direct pricing and post-sales support from nearly every ISP, VoIP and Cloud Provider.</p>
  <div class="btn btn-hero">Read More</div>
  <div class="dots"><span></span><span></span><span class="on"></span><span></span><span></span></div>
</section>

<section class="solutions">
  <h2 class="heading section-title" style="top:50px">Technology Solutions</h2>
  <div class="title-rule" style="top:105px"></div>

  <article class="sol-card" style="left:130px">
    <svg width="64" height="64" viewBox="0 0 64 64" fill="none" stroke="#0b4ea2" stroke-width="4"><path d="M32 18l12 7v14l-12 7-12-7V25z"/><path d="M20 25l12 7 12-7M32 32v14"/><circle cx="32" cy="6" r="3.5" fill="#0b4ea2"/><circle cx="32" cy="58" r="3.5" fill="#0b4ea2"/><circle cx="8" cy="18" r="3.5" fill="#0b4ea2"/><circle cx="56" cy="18" r="3.5" fill="#0b4ea2"/><circle cx="8" cy="46" r="3.5" fill="#0b4ea2"/><circle cx="56" cy="46" r="3.5" fill="#0b4ea2"/></svg>
    <h3>Data &amp; Network</h3>
    <p>Businesses have a variety of data and connectivity requirements</p>
    <div class="btn">Read More</div>
  </article>
  <article class="sol-card" style="left:370px">
    <svg width="64" height="64" viewBox="0 0 64 64" fill="#0b4ea2"><rect x="22" y="2" width="20" height="36" rx="10"/><path d="M14 28a18 18 0 0 0 36 0h-5a13 13 0 0 1-26 0z"/><rect x="29" y="46" width="6" height="10"/><rect x="20" y="56" width="24" height="5"/></svg>
    <h3>Voice Services</h3>
    <p>Voice and communications technology is constantly evolving</p>
    <div class="btn">Read More</div>
  </article>
  <article class="sol-card" style="left:609px">
    <svg width="64" height="64" viewBox="0 0 64 64" fill="#0b4ea2"><path d="M16 24a10 10 0 0 1 10-14 12 12 0 0 1 22 4 8 8 0 0 1 0 14H18a7 7 0 0 1-2-4z"/><rect x="30" y="28" width="4" height="8"/><rect x="10" y="36" width="44" height="3"/><rect x="10" y="36" width="3" height="6"/><rect x="30" y="36" width="4" height="6"/><rect x="51" y="36" width="3" height="6"/><rect x="4" y="42" width="15" height="20"/><rect x="24" y="42" width="16" height="20"/><rect x="45" y="42" width="15" height="20"/></svg>
    <h3>Data Center &amp; Cloud</h3>
    <p>IFf you are seeking the most cost-effective and reliable way to back up</p>
    <div class="btn">Read More</div>
  </article>
  <article class="sol-card" style="left:849px">
    <svg width="64" height="64" viewBox="0 0 64 64" fill="#0b4ea2"><path d="M10 8l10-2 6 12-6 5a30 30 0 0 0 16 16l5-6 12 6-2 10c-26 2-44-16-41-41z"/><path d="M32 6h28v18H44l-8 6v-6h-4z"/><rect x="37" y="12" width="18" height="2" fill="#fff"/><rect x="37" y="17" width="12" height="2" fill="#fff"/></svg>
    <h3>TechCircle</h3>
    <p>Welcome Circle members! If you are in the market for a new ISP, Phone System.</p>
    <div class="btn">Read More</div>
  </article>
</section>

<section class="value">
  <h2>More than<br>“Best Price”.</h2>
  <p class="lead">World-class post-sales support and lifecycle management.</p>
  <div class="btn btn-value">Get Quotes</div>

  <div class="tile" style="left:576px;top:61px"><svg width="46" height="40" viewBox="0 0 46 40" fill="#0b4ea2"><path d="M2 6h24v16H12l-7 6v-6H2z"/><path d="M20 2h24v16h-3v6l-7-6H29V4h-9z"/></svg>Consulting &amp; Solution<br>Recommendations</div>
  <div class="tile" style="left:743px;top:61px"><svg width="40" height="40" viewBox="0 0 40 40" fill="#0b4ea2"><path d="M4 30L30 4l6 6-26 26H4z"/><path d="M6 4l30 30-4 4L2 8z" opacity=".75"/></svg><br>Plan &amp; design</div>
  <div class="tile" style="left:910px;top:61px"><svg width="40" height="40" viewBox="0 0 40 40" fill="none" stroke="#0b4ea2" stroke-width="4"><path d="M30 22v14H4V8h14"/><path d="M34 4l4 4-18 18h-4v-4z" fill="#0b4ea2"/></svg>Contract<br>Negotiations</div>
  <div class="tile" style="left:576px;top:199px"><svg width="50" height="40" viewBox="0 0 50 40" fill="#0b4ea2"><circle cx="25" cy="6" r="5"/><rect x="19" y="12" width="12" height="10" rx="3"/><rect x="24" y="22" width="2" height="6"/><rect x="8" y="27" width="34" height="2"/><circle cx="8" cy="34" r="4" fill="none" stroke="#0b4ea2" stroke-width="2.5"/><circle cx="25" cy="34" r="4" fill="none" stroke="#0b4ea2" stroke-width="2.5"/><circle cx="42" cy="34" r="4" fill="none" stroke="#0b4ea2" stroke-width="2.5"/></svg>Project<br>Management</div>
  <div class="tile" style="left:743px;top:199px"><svg width="44" height="40" viewBox="0 0 44 40" fill="none" stroke="#0b4ea2" stroke-width="5"><circle cx="28" cy="13" r="6" stroke-dasharray="4 3"/><circle cx="12" cy="28" r="6" stroke-dasharray="4 3"/></svg>Post Install<br>support escalations</div>
  <div class="tile" style="left:910px;top:199px"><svg width="40" height="40" viewBox="0 0 40 40" fill="none" stroke="#0b4ea2" stroke-width="4"><path d="M8 20A12 12 0 0 1 30 12"/><path d="M32 20A12 12 0 0 1 10 28"/><path d="M30 4v9h-9M10 36v-9h9"/></svg>Renewal<br>Negotiations</div>
  <div class="tile" style="left:743px;top:341px"><svg width="40" height="40" viewBox="0 0 40 40" fill="#0b4ea2"><circle cx="20" cy="11" r="9"/><path d="M4 38a16 14 0 0 1 32 0z"/></svg>Ongoing Supplier<br>Review Check Ins</div>
</section>

<section class="consult">
  <h2 class="heading section-title">Unbiased, free consulting &amp;<br>design from industry veterans.</h2>
  <div class="title-rule" style="top:1820px"></div>

  <article class="adv-card" style="left:164px">
    <svg width="64" height="72" viewBox="0 0 64 72" fill="#f7841e"><circle cx="32" cy="26" r="22"/><circle cx="32" cy="26" r="14" fill="#fff"/><circle cx="32" cy="26" r="10"/><path d="M16 42l-10 20 10-2 5 9 9-22zM48 42l10 20-10-2-5 9-9-22z"/></svg>
    <h3>Trusted Advisor</h3>
    <p>Take advantage of our longstanding relationships with hundreds of ISP, VoIP, and Cloud providers for better-than-direct pricing and enhanced post-sales support / e scalation channels.</p>
  </article>
  <article class="adv-card" style="left:465px">
    <svg width="72" height="72" viewBox="0 0 72 72"><circle cx="36" cy="36" r="32" fill="#f7841e"/><circle cx="36" cy="36" r="25" fill="#fff"/><path d="M18 32c6-10 18-14 28-8 6 4 8 14 2 20-4 4-10 2-14 6-4 4-12 2-14-4-2-4-4-8-2-14z" fill="#f7841e"/></svg>
    <h3>Global Reach</h3>
    <p>Deep product reach from hundreds of world-class service providers gives you a competitive edge on a global scale.</p>
  </article>
  <article class="adv-card" style="left:766px">
    <svg width="72" height="72" viewBox="0 0 72 72" fill="none" stroke="#fff" stroke-width="3"><circle cx="36" cy="36" r="32" fill="#f7841e" stroke="none"/><ellipse cx="36" cy="36" rx="14" ry="32"/><path d="M4 36h64M36 4v64M10 20h52M10 52h52"/></svg>
    <h3>Right-Fit Technology</h3>
    <p>We’ve seen it all. Our expertise and experience span geographies, suppliers, industries, and verticals which means you’ll get unbiased recommendations designed to solve your problems.</p>
  </article>
</section>

<section class="testimonials">
  <h2 class="heading section-title" style="top:52px">Testimonials</h2>
  <div class="title-rule" style="top:108px"></div>
  <div class="arrow" style="left:70px;top:302px">‹</div>
  <div class="arrow" style="left:1098px;top:302px">›</div>

  <article class="quote-card" style="left:132px">
    <div class="qmark">“</div>
    <p>I want to give long-overdue accolades to Linkvantor. We became acquainted on the TechCircle forums as I searched for guidance on ISPs that best suited our business interests. The Linkvantor team’s honest, straightforward, and knowledgeable approach was more than we could’ve asked for or anticipated.</p>
    <div class="qend" style="margin-right:150px">”</div>
    <div class="who"><b>Marco Delaney,</b><br>IT Service Provider</div>
  </article>
  <article class="quote-card" style="left:450px">
    <div class="qmark">“</div>
    <p>I have worked with Linkvantor on several occasions, and they always come through for us. They are very responsive and are currently facilitating cancellation of two T1 connections in different locations and reconnecting in a 3rd location. Linkvantor is now my one stop shop for data/telco service</p>
    <div class="who"><b>Owen Pritchard</b><br>IT Director</div>
  </article>
  <article class="quote-card" style="left:766px">
    <div class="qmark">“</div>
    <p>I have recently been working with Linkvantor to assist with providing communications services to client offices in the US. Their level of customer service has been excellent, with rapid responses to questions and requests. They have done a great job of providing numerous options, and have been very patient</p>
    <div class="qend" style="margin-top:-22px">”</div>
    <div class="who"><b>Dale Whitfield</b><br>IT Director</div>
  </article>
</section>

<section class="partners">
  <h2 class="heading section-title">Our Partners</h2>
  <div class="title-rule" style="top:2935px"></div>
  <div class="arrow" style="left:70px;top:2985px">‹</div>
  <div class="arrow" style="left:1098px;top:2985px">›</div>
  <div class="logos">
    <span class="logo-name"><i></i>Arcway</span>
    <span class="logo-name">Nexel Networks</span>
    <span class="logo-name">Allora</span>
    <span class="logo-name">Fernpoint</span>
    <span class="logo-name"><i></i>Corvast</span>
    <span class="logo-name">Kestrel</span>
  </div>
</section>

<section class="quote-form">
  <h2 class="heading section-title" style="color:#fff">Get a Quote</h2>
  <div class="title-rule"></div>
  <div class="field" style="left:288px;top:154px;width:304px;height:47px">Name</div>
  <div class="field" style="left:609px;top:154px;width:306px;height:47px">E Mail</div>
  <div class="field" style="left:288px;top:222px;width:304px;height:47px">Phone</div>
  <div class="field" style="left:609px;top:222px;width:306px;height:47px">Subject</div>
  <div class="field" style="left:288px;top:288px;width:627px;height:104px">Message</div>
  <div class="btn btn-send">Get Quotes</div>
</section>

<footer class="site-footer">
  <div class="footer-brand">Linkvantor</div>
  <div class="footer-col" style="left:445px">
    <h4>MENU</h4>
    <ul><li>TECHNOLOGY SOLUTIONS</li><li>SUPPLIERS</li><li>PARTNERSHIP</li><li>TESTIMONIALS</li><li>REQUEST A QUOTE</li><li>CONTACT US</li></ul>
  </div>
  <div class="footer-col" style="left:680px">
    <h4>CONTACT US</h4>
    <div class="contact-row"><span class="circ"><svg width="14" height="14" viewBox="0 0 24 24"><path fill="#1c1819" d="M6.6 10.8a15.1 15.1 0 0 0 6.6 6.6l2.2-2.2c.3-.3.7-.4 1-.2 1.1.4 2.3.6 3.6.6.6 0 1 .4 1 1V20c0 .6-.4 1-1 1A17 17 0 0 1 3 4c0-.6.4-1 1-1h3.5c.6 0 1 .4 1 1 0 1.3.2 2.5.6 3.6.1.3 0 .7-.2 1z"/></svg></span><span>Call Us<br>1-888-555-0142</span></div>
    <div class="contact-row"><span class="circ"><svg width="14" height="12" viewBox="0 0 14 12"><rect x="0" y="1" width="14" height="10" fill="#1c1819"/><path d="M0 1l7 6 7-6" stroke="#fff" fill="none"/></svg></span><span>E mail Us<br>team@linkvantor.example</span></div>
  </div>
  <div class="footer-col" style="left:941px">
    <h4>FOLLOW US</h4>
    <div class="contact-row"><span class="circ"></span><span>Like us on<br>SOCIAL PROFILE</span></div>
    <div class="contact-row"><span class="circ"></span><span>Follow us on<br>SOCIAL FEED</span></div>
    <div class="contact-row"><span class="circ"></span><span>Follow us on<br>PRO PROFILE</span></div>
  </div>
  <div class="footer-rule"></div>
  <div class="copyright">Copyright © 2020 All Rights Reserved</div>
</footer>

</body>
</html>
```